Business Cards and Logo needed for Rum Website

I need a smart, modern but fun business card (and Logo) to help promote my website BrightBarrelNotes.com

The website contains reviews of Rum (and eventually other spirits) as well as news and blog posts.

I would like a 2-sided design, with the logo and company name on one side and text on the other.

Text fields required are:
Name (Dan Fowler)
Website (www.brightbarrelnotes.com)
Email (dan@brightbarrelnotes.com)
Twitter (@BrightBarrelNotes)

For the logo i'm open to suggestions however it must incorporate a wooden Cask and a number of Stars. Ideas so far have been for a Cask surrounded in a number of Stars forming a circle around it with the text Bright Barrel Notes underneath. The logo should be modern but also a little bit cartoony and stylised. General drink/spirits themes will also be considered.

Colours: I like the idea of yellow text with black background but again i'm open to suggestions on what would work well. Contrasting colours for the 2-sides would be good.

Cards will be printed via Pelv.com so please consult their style guidelines if required: http://uk.pelv.com/help/faq/templates-and-guidelines.html

Requirements
Must have
• A spirits Cask
A number of Stars (preferrably yellow or gold)

```html
<!DOCTYPE html>
<html lang="en">
<head>
<meta charset="UTF-8">
<title>Bright Barrel Notes — Business Card</title>
<link rel="stylesheet" href="https://fonts.googleapis.com/css2?family=Jost:wght@400&display=swap">
<style>
  :root {
    --stage: #000000;
    --wood-dark-1: #5b554c;
    --wood-dark-2: #77716a;
    --wood-dark-3: #4c463e;
    --wood-light-1: #d9d4c6;
    --wood-light-2: #eeebe2;
    --wood-light-3: #c9c2b0;
    --cask-shade: rgba(38, 28, 18, 0.82);
    --star-yellow: #e9e77c;
    --ink-brown: #4a2810;
  }
  * { margin: 0; padding: 0; box-sizing: border-box; }
  html, body {
    width: 1200px;
    height: 900px;
    overflow: hidden;
    background: var(--stage);
  }
  .sheet {
    position: relative;
    width: 1200px;
    height: 900px;
  }
  .card {
    position: absolute;
    left: 300px;
    width: 600px;
    border-radius: 15px;
    overflow: hidden;
  }
  .card--front {
    top: 75px;
    height: 343px;
  }
  .card--back {
    top: 483px;
    height: 342px;
  }
  .wood {
    position: absolute;
    inset: 0;
  }
  .wood--weathered-grey {
    background: linear-gradient(180deg,
      var(--wood-dark-2) 0%, var(--wood-dark-1) 18%,
      var(--wood-dark-2) 38%, var(--wood-dark-3) 55%,
      var(--wood-dark-2) 75%, var(--wood-dark-1) 100%);
  }
  .wood--bleached {
    background: linear-gradient(180deg,
      var(--wood-light-2) 0%, var(--wood-light-1) 30%,
      var(--wood-light-2) 55%, var(--wood-light-3) 80%,
      var(--wood-light-1) 100%);
  }
  .brand-mark {
    position: absolute;
    left: 28px;
    top: 48px;
    width: 256px;
    height: 256px;
    border-radius: 50%;
    background: var(--cask-shade);
    display: flex;
    align-items: center;
    justify-content: center;
  }
  .brand-name {
    font-family: "Jost", "Futura", sans-serif;
    font-weight: 400;
    font-size: 23px;
    letter-spacing: 1.5px;
    color: var(--star-yellow);
    text-align: center;
    line-height: 1.2;
  }
  .contact {
    position: absolute;
    right: 22px;
    bottom: 16px;
    list-style: none;
    text-align: right;
    font-family: "Jost", "Futura", sans-serif;
    font-weight: 400;
    font-size: 20px;
    letter-spacing: 2px;
    line-height: 31px;
    color: var(--ink-brown);
  }
</style>
</head>
<body>
  <main class="sheet">
    <section class="card card--front" aria-label="Card front">
      <div class="wood wood--weathered-grey" role="img" aria-label="Photograph of weathered grey wooden deck planks"></div>
      <div class="brand-mark">
        <p class="brand-name">Bright Barrel Notes</p>
      </div>
    </section>

    <section class="card card--back" aria-label="Card back">
      <div class="wood wood--bleached" role="img" aria-label="Photograph of bleached, cracked wooden boards"></div>
      <ul class="contact">
        <li class="contact__name">Name: Dan Fowler</li>
        <li class="contact__website">Website: www.brightbarrelnotes.com</li>
        <li class="contact__email">Email dan@brightbarrelnotes.com</li>
        <li class="contact__twitter">Twitter: @BrightBarrelNotes</li>
      </ul>
    </section>
  </main>
</body>
</html>
```